Property Consultancy require stationary

Property Consultancy K7 Group Ltd, slogan is Bright Harbour Allies. Require letterhead, business card and Outlook email signature utilising existing logo design.

Property

```html
<!DOCTYPE html>
<html lang="en">
<head>
<meta charset="utf-8">
<title>K7 Group Ltd — Letterhead</title>
<link href="https://fonts.googleapis.com/css2?family=Exo+2:wght@400;600;700&family=Alex+Brush&display=swap" rel="stylesheet">
<style>
  :root {
    --bg: #f2f2f2;
    --paper: #fdfdfd;
    --red: #e2393b;
    --grey: #8a8a8a;
    --text: #6b6b6b;
    --dark: #2b2b2b;
    --rule: #b5b5b5;
  }
  * { margin: 0; padding: 0; box-sizing: border-box; }
  html, body { width: 1200px; height: 1000px; overflow: hidden; }
  body {
    background: var(--bg);
    font-family: "Exo 2", sans-serif;
    color: var(--text);
    position: relative;
  }
  .letterhead {
    position: absolute;
    top: 190px;
    width: 440px;
    height: 616px;
    background: var(--paper);
  }
  .letterhead--first { left: 132px; }
  .letterhead--second { left: 612px; }

  .edge-band {
    position: absolute; left: 0; top: 0;
    width: 11px; height: 100%;
    background: var(--red);
  }
  .brand {
    position: absolute; right: 14px; top: 24px;
    text-align: right;
  }
  .brand__name {
    font-weight: 700; font-size: 17px; letter-spacing: 0.5px;
    color: var(--red); line-height: 1;
  }
  .brand__tagline {
    font-size: 4.6px; letter-spacing: 0.6px; text-transform: uppercase;
    color: var(--grey); margin-top: 3px;
  }
  .content-rule {
    position: absolute; left: 98px; top: 160px;
    width: 1px; height: 310px; background: var(--rule);
  }
  .letter {
    position: absolute; left: 119px; top: 160px; width: 298px;
  }
  .letter__title {
    font-size: 11px; color: var(--grey); font-weight: 400; white-space: nowrap;
  }
  .letter__title strong { color: var(--red); font-weight: 700; }
  .letter__body {
    margin-top: 24px;
    font-size: 5.6px; line-height: 10.6px; text-align: justify;
  }
  .letter__body p + p { margin-top: 8px; }
  .letter__body p.gap { margin-top: 20px; }

  .meta {
    position: absolute; left: 29px; top: 284px;
    font-size: 7.5px; line-height: 8px;
  }
  .meta dt { color: var(--red); font-weight: 700; text-transform: uppercase; }
  .meta dd { color: var(--grey); margin-bottom: 5px; }

  .side-marker {
    position: absolute; right: 4px; top: 300px;
    width: 10px; height: 16px; background: var(--red);
  }
  .sign-off {
    position: absolute; left: 290px; top: 467px; width: 120px; text-align: center;
  }
  .sign-off__role { font-size: 7px; color: var(--grey); }
  .sign-off__name {
    font-family: "Alex Brush", cursive; font-size: 21px; color: var(--dark);
    margin-top: 6px;
  }
  .footer {
    position: absolute; left: 51px; top: 585px;
    display: flex; font-size: 4.6px; line-height: 5.6px; color: var(--text);
  }
  .footer__company { position: absolute; top: 0; left: 0; color: var(--red); font-weight: 600; white-space: nowrap; }
  .footer__col { display: flex; gap: 3px; margin-top: 6px; }
  .footer__col--contact { border-left: 1px solid var(--rule); margin-left: 8px; padding-left: 8px; flex-direction: column; gap: 0; }
  .footer__line { display: flex; align-items: center; gap: 3px; white-space: nowrap; }
  .icon { width: 5px; height: 5px; flex: none; }
</style>
</head>
<body>

  <article class="letterhead letterhead--first">
    <div class="edge-band"></div>
    <div class="brand">
      <div class="brand__name">K7 GROUP</div>
      <div class="brand__tagline">Bright Harbour Allies</div>
    </div>
    <div class="content-rule"></div>
    <section class="letter">
      <h1 class="letter__title"><strong>Nulla sodales:</strong> Lorem ipsum dolor sit ametconsectetur.</h1>
      <div class="letter__body">
        <p>Dear Client,</p>
        <p>Lorem ipsum dolor sit amet, consectetur adipiscing elit. Nulla sodales nisi vitae Lorem ipsum dolor sit amet, consectetur adipiscing elit. Suspendisse feugiat eros nisl, a facilisis risus eleifend sed. Aliquam mauris enim, fermentum eu lacinia sit amet, laoreet eu leo. Nullam eleifend nulla in libero tristique, ac vulputate odio tincidunt. Etiam non condimentum tortor. Integer suscipit neque nec odio porttitor cursus. Phasellus a sapien blandit, suscipit justo id, condimentum ante. Morbi tristique justo risus, id mattis dui molestie ut. Nullam volutpat ut quam commodo faucibus. Pellentesque urna est, interdum in elit quis, pharetra elementum orci. Nam pharetra velit molestie justo placerat scelerisque.</p>
        <p class="gap">Ut vitae interdum diam, in euismod ante. Pellentesque volutpat, risus sit amet sodales hendrerit, mi turpis vulputate dolor, eget cursus nulla eros nec tellus. Nulla tincidunt molestie libero vel pretium. Donec condimentum nulla sit amet risus semper imperdiet. Duis congue eros nec diam blandit, et pellentesque sapien auctor. Curabitur iaculis enim lectus, in imperdiet mauris mattis eget. Etiam ac ornare metus. Mauris risus leo, egestas at dolor a, ultrices adipiscing est. Nunc faucibus scelerisque mollis. Pellentesque aliquet mauris tellus, id dignissim risus viverra et. Mauris venenatis lobortis eros. Nam id diam in ligula malesuada feugiat. Cras turpis felis, aliquet id mauris elementum, feugiat ultricies nisl.</p>
        <p>Best regards.</p>
      </div>
    </section>
    <dl class="meta">
      <dt>Subject</dt><dd>lorem ipsum</dd>
      <dt>Date</dt><dd>01/01/2014</dd>
      <dt>Adressed to</dt><dd>John Doe</dd>
    </dl>
    <div class="side-marker"></div>
    <div class="sign-off">
      <div class="sign-off__role">Director</div>
      <div class="sign-off__name">Martin Hale</div>
    </div>
    <footer class="footer">
      <div class="footer__company">K7 Group Limited</div>
      <div class="footer__col">
        <svg class="icon" viewBox="0 0 10 10"><path d="M5 0.5a3.2 3.2 0 0 0-3.2 3.2C1.8 6.2 5 9.5 5 9.5s3.2-3.3 3.2-5.8A3.2 3.2 0 0 0 5 .5zm0 4.5a1.3 1.3 0 1 1 0-2.6 1.3 1.3 0 0 1 0 2.6z" fill="var(--red)"/></svg>
        <div>PO Box 20418<br>Riverton</div>
      </div>
      <div class="footer__col footer__col--contact">
        <div class="footer__line"><svg class="icon" viewBox="0 0 10 10"><path d="M2 1l2 .3.6 2-1.2 1a5.5 5.5 0 0 0 2.3 2.3l1-1.2 2 .6.3 2C8.8 9 8 9.3 7 9 4 8 2 6 1 3 .7 2 1 1.2 2 1z" fill="var(--red)"/></svg>+64 3 555-0148</div>
        <div class="footer__line"><svg class="icon" viewBox="0 0 10 10"><circle cx="5" cy="5" r="4" fill="none" stroke="var(--red)" stroke-width="1.4"/><path d="M1 5h8M5 1c-2 2.5-2 5.5 0 8M5 1c2 2.5 2 5.5 0 8" fill="none" stroke="var(--red)" stroke-width=".8"/></svg>www.k7group.example</div>
      </div>
    </footer>
  </article>

  <article class="letterhead letterhead--second">
    <div class="edge-band"></div>
    <div class="brand">
      <div class="brand__name">K7 GROUP</div>
      <div class="brand__tagline">Bright Harbour Allies</div>
    </div>
    <div class="content-rule"></div>
    <section class="letter">
      <h1 class="letter__title"><strong>Nulla sodales:</strong> Lorem ipsum dolor sit ametconsectetur.</h1>
      <div class="letter__body">
        <p>Dear Client,</p>
        <p>Lorem ipsum dolor sit amet, consectetur adipiscing elit. Nulla sodales nisi vitae Lorem ipsum dolor sit amet, consectetur adipiscing elit. Suspendisse feugiat eros nisl, a facilisis risus eleifend sed. Aliquam mauris enim, fermentum eu lacinia sit amet, laoreet eu leo. Nullam eleifend nulla in libero tristique, ac vulputate odio tincidunt. Etiam non condimentum tortor. Integer suscipit neque nec odio porttitor cursus. Phasellus a sapien blandit, suscipit justo id, condimentum ante. Morbi tristique justo risus, id mattis dui molestie ut. Nullam volutpat ut quam commodo faucibus. Pellentesque urna est, interdum in elit quis, pharetra elementum orci. Nam pharetra velit molestie justo placerat scelerisque.</p>
        <p class="gap">Ut vitae interdum diam, in euismod ante. Pellentesque volutpat, risus sit amet sodales hendrerit, mi turpis vulputate dolor, eget cursus nulla eros nec tellus. Nulla tincidunt molestie libero vel pretium. Donec condimentum nulla sit amet risus semper imperdiet. Duis congue eros nec diam blandit, et pellentesque sapien auctor. Curabitur iaculis enim lectus, in imperdiet mauris mattis eget. Etiam ac ornare metus. Mauris risus leo, egestas at dolor a, ultrices adipiscing est. Nunc faucibus scelerisque mollis. Pellentesque aliquet mauris tellus, id dignissim risus viverra et. Mauris venenatis lobortis eros. Nam id diam in ligula malesuada feugiat. Cras turpis felis, aliquet id mauris elementum, feugiat ultricies nisl.</p>
        <p>Best regards.</p>
      </div>
    </section>
    <dl class="meta">
      <dt>Subject</dt><dd>lorem ipsum</dd>
      <dt>Date</dt><dd>01/01/2014</dd>
      <dt>Adressed to</dt><dd>John Doe</dd>
    </dl>
    <div class="side-marker"></div>
    <div class="sign-off">
      <div class="sign-off__role">Director</div>
      <div class="sign-off__name">Martin Hale</div>
    </div>
    <footer class="footer">
      <div class="footer__company">K7 Group Limited</div>
      <div class="footer__col">
        <svg class="icon" viewBox="0 0 10 10"><path d="M5 0.5a3.2 3.2 0 0 0-3.2 3.2C1.8 6.2 5 9.5 5 9.5s3.2-3.3 3.2-5.8A3.2 3.2 0 0 0 5 .5zm0 4.5a1.3 1.3 0 1 1 0-2.6 1.3 1.3 0 0 1 0 2.6z" fill="var(--red)"/></svg>
        <div>PO Box 20418<br>Riverton</div>
      </div>
      <div class="footer__col footer__col--contact">
        <div class="footer__line"><svg class="icon" viewBox="0 0 10 10"><path d="M2 1l2 .3.6 2-1.2 1a5.5 5.5 0 0 0 2.3 2.3l1-1.2 2 .6.3 2C8.8 9 8 9.3 7 9 4 8 2 6 1 3 .7 2 1 1.2 2 1z" fill="var(--red)"/></svg>+64 3 555-0148</div>
        <div class="footer__line"><svg class="icon" viewBox="0 0 10 10"><circle cx="5" cy="5" r="4" fill="none" stroke="var(--red)" stroke-width="1.4"/><path d="M1 5h8M5 1c-2 2.5-2 5.5 0 8M5 1c2 2.5 2 5.5 0 8" fill="none" stroke="var(--red)" stroke-width=".8"/></svg>www.k7group.example</div>
      </div>
    </footer>
  </article>

</body>
</html>
```